Hi everyone,
Bright Nest Homes is a business that renovates older houses into modern homes. I'm looking for a design that is clean and simple. It needs to show the client that renovating is a simple process. No more than 3 colours to be used thanks.

What I need:
1. Logo
2. Business card (one side)
3. Letter head (A4)

Looking forward to the designs!

Industry/Entity Type

Construction

Logo Text

Bright Nest Homes

Font styles to use
Sans Serif

Requirements
Must have
• Trading name: Bright Nest Homes
• Contact name: Declan Ferris
• Email: declanferris@brightnesthomes.com.au
• Tel: 0417 582 046
• Clean and simple
Nice to have
• If design might include a few tools. eg Hammer, paint roller etc.
Should not have
• Complicated design

```html
<!DOCTYPE html>
<html lang="en">
<head>
<meta charset="utf-8">
<title>Bright Nest Homes – Stationery</title>
<link rel="stylesheet" href="https://fonts.googleapis.com/css2?family=Roboto+Condensed:wght@300;400;700&family=Open+Sans:wght@400&display=swap">
<style>
  :root {
    --stage: #000000;
    --paper: #ffffff;
    --brand-orange: #f39321;
    --brand-charcoal: #424244;
    --label: #ffffff;
  }
  * { box-sizing: border-box; margin: 0; padding: 0; }
  html, body { width: 1200px; height: 978px; overflow: hidden; background: var(--stage); }
  .board { position: relative; width: 1200px; height: 978px; background: var(--stage); }

  .sheet { position: absolute; background: var(--paper); overflow: hidden; }
  .caption {
    position: absolute; transform: translateX(-50%);
    font-family: "Open Sans", sans-serif; font-size: 10.5px; color: var(--label);
    letter-spacing: -0.2px; white-space: nowrap;
  }

  .wordmark {
    position: absolute; display: flex; align-items: center; gap: 0.3em;
    font-family: "Roboto Condensed", sans-serif; font-weight: 700;
    color: var(--brand-charcoal); white-space: nowrap; line-height: 1;
  }
  .wordmark__square { width: 0.55em; height: 0.55em; background: var(--brand-orange); flex: none; }

  .contact-line {
    display: flex; align-items: center; justify-content: center; gap: 8px;
    font-family: "Roboto Condensed", sans-serif; font-weight: 300; color: var(--paper);
    white-space: nowrap;
  }
  .contact-line svg { display: block; flex: none; }

  /* Letterhead */
  .letterhead { left: 72px; top: 176px; width: 499px; height: 645px; }
  .letterhead .wordmark { left: 29px; top: 40px; font-size: 26px; }
  .letterhead__rule { position: absolute; left: 0; top: 609px; width: 100%; height: 4px; background: var(--brand-charcoal); }
  .letterhead__footer { position: absolute; left: 0; top: 613px; width: 100%; height: 32px; background: var(--brand-orange); }
  .letterhead__footer .contact-line { height: 100%; font-size: 12.5px; }

  /* Logo panel */
  .logo-panel { left: 633px; top: 184px; width: 502px; height: 297px; }
  .logo-panel .wordmark { left: 50%; top: 50%; transform: translate(-50%, -50%); font-size: 48px; }

  /* Business card */
  .business-card { left: 666px; top: 539px; width: 441px; height: 253px; }
  .business-card .wordmark { left: 50%; top: 70px; transform: translateX(-50%); font-size: 34px; }
  .business-card__name-band {
    position: absolute; left: 0; top: 137px; width: 100%; height: 32px; background: var(--brand-charcoal);
    display: flex; align-items: center; justify-content: center;
    font-family: "Roboto Condensed", sans-serif; font-weight: 700; font-size: 23px;
    color: var(--paper); letter-spacing: 0.3px; text-transform: uppercase;
  }
  .business-card__contact { position: absolute; left: 0; top: 169px; width: 100%; height: 84px; background: var(--brand-orange); }
  .business-card__contact .contact-line { margin-top: 20px; font-size: 14.5px; }
</style>
</head>
<body>
<main class="board">

  <section class="sheet letterhead" aria-label="Letterhead">
    <div class="wordmark"><span class="wordmark__square"></span>Bright Nest Homes</div>
    <div class="letterhead__rule"></div>
    <footer class="letterhead__footer">
      <p class="contact-line">
        <span>declanferris@brightnesthomes.com.au</span>
        <svg width="22" height="12" viewBox="0 0 22 12" aria-hidden="true"><rect x="0.5" y="0.5" width="21" height="11" fill="#fff"/><path d="M0.5 0.5 L11 7 L21.5 0.5" fill="none" stroke="#f39321" stroke-width="1"/></svg>
        <span>0417 582 046</span>
        <svg width="8" height="14" viewBox="0 0 8 14" aria-hidden="true"><path d="M1 1 Q7 0 7 7 Q7 14 1 13 L2 10 Q4 10 4 7 Q4 4 2 4 Z" fill="#fff"/></svg>
      </p>
    </footer>
  </section>
  <p class="caption" style="left:320px; top:835px;">LETTER HEAD</p>

  <section class="sheet logo-panel" aria-label="Logo">
    <div class="wordmark"><span class="wordmark__square"></span>Bright Nest Homes</div>
  </section>
  <p class="caption" style="left:893px; top:497px;">LOGO</p>

  <section class="sheet business-card" aria-label="Business card">
    <div class="wordmark"><span class="wordmark__square"></span>Bright Nest Homes</div>
    <h1 class="business-card__name-band">Declan Ferris</h1>
    <div class="business-card__contact">
      <p class="contact-line">
        <span>declanferris@brightnesthomes.com.au</span>
        <svg width="24" height="13" viewBox="0 0 24 13" aria-hidden="true"><rect x="0.5" y="0.5" width="23" height="12" fill="#fff"/><path d="M0.5 0.5 L12 7.5 L23.5 0.5" fill="none" stroke="#f39321" stroke-width="1"/></svg>
        <span>0417 582 046</span>
        <svg width="9" height="16" viewBox="0 0 8 14" aria-hidden="true"><path d="M1 1 Q7 0 7 7 Q7 14 1 13 L2 10 Q4 10 4 7 Q4 4 2 4 Z" fill="#fff"/></svg>
      </p>
    </div>
  </section>
  <p class="caption" style="left:882px; top:815px;">BUSINESS CARD</p>

</main>
</body>
</html>
```